Flyer-Design für Empowerment-Coaching
Sehr schnelle Auffassungsgabe, schnelles Hineinfinden in mein Projekt und vorausschauendes Denken. Schnelles und zuverlässiges Arbeiten, sehr netter Kontakt, bin äußerst zufrieden und Kann Valmora nur weiterempfehlen!
Zielgruppe
Ich bin Empowerment-Coach für KLAR-Macher, das sind Frauen (zwischen 30-55, angestellt in vorrangig Assistenzfunktionen), die zu nett sind, um nein zu sagen und sich freundlich und selbstbestimmt im Business zu behaupten. Meine Leistungen biete ich vorrangig im Online-Coaching (1:1, Mastermind), aber auch Workshops.
Aufgabenstellung
Farben sollten Webseite und zum Logo passen:
#7AB51D, CMYK: 60/0/100/0
Grau: #707173, CMYK: 0/0/0/70, siehe auch www.beratung-fuer-klarmacher.de

```html
<!DOCTYPE html>
<html lang="de">
<head>
<meta charset="utf-8">
<title>Be B.R.A.V.E. – Coaching für Klarmacher</title>
<link href="https://fonts.googleapis.com/css2?family=Source+Sans+3:wght@400;600;700&family=Permanent+Marker&display=swap" rel="stylesheet">
<style>
  :root {
    --green: #7ab51d;
    --green-deep: #5f9416;
    --grey: #707173;
    --grey-band: rgba(72, 73, 75, 0.88);
    --bg-light: #ececec;
    --bg-mid: #cfcfd0;
    --white: #ffffff;
    --brush: "Permanent Marker", "Arial Black", sans-serif;
    --sans: "Source Sans 3", "Myriad Pro", sans-serif;
  }
  html, body {
    margin: 0;
    padding: 0;
    overflow: hidden;
    background: var(--white);
  }
  .flyer {
    position: relative;
    width: 1200px;
    height: 851px;
    overflow: hidden;
    font-family: var(--sans);
    background: radial-gradient(ellipse at 70% 35%, var(--bg-light) 0%, #dcdcdd 55%, var(--bg-mid) 100%);
  }
  .hero-photo {
    position: absolute;
    left: 0;
    top: 0;
    width: 820px;
    height: 682px;
    background:
      radial-gradient(ellipse 30% 36% at 38% 30%, #d9b7a4 0%, rgba(217,183,164,0) 70%),
      radial-gradient(ellipse 45% 55% at 25% 45%, #4a3a33 0%, rgba(74,58,51,0) 70%),
      radial-gradient(ellipse 60% 35% at 30% 100%, #9a9a9c 0%, rgba(154,154,156,0) 70%);
    opacity: 0.75;
  }
  .logo-box {
    position: absolute;
    left: 724px;
    top: 55px;
    width: 476px;
    height: 203px;
    background: var(--white);
    display: flex;
    align-items: center;
    justify-content: center;
    gap: 18px;
  }
  .logo-dot {
    width: 70px;
    height: 70px;
    border-radius: 50%;
    background: var(--green);
  }
  .logo-name {
    font-size: 36px;
    font-weight: 600;
    color: var(--grey);
    line-height: 1.05;
  }
  .headline {
    position: absolute;
    left: 0;
    top: 380px;
    width: 600px;
    height: 290px;
    margin: 0;
  }
  .headline text {
    font-family: var(--brush);
    font-weight: 400;
    fill: var(--white);
  }
  .footer-band {
    position: absolute;
    left: 0;
    top: 682px;
    width: 1200px;
    height: 169px;
    background: var(--grey-band);
    color: var(--white);
    font-size: 22px;
    line-height: 32px;
  }
  .footer-col { position: absolute; top: 33px; }
  .footer-col--address { left: 48px; }
  .footer-col--phone { left: 391px; }
  .footer-col--web { left: 721px; top: 65px; }
  .footer-col p { margin: 0; }
  .label { display: inline-block; width: 92px; }
  .offer-badge {
    position: absolute;
    left: 740px;
    top: 428px;
    width: 450px;
    height: 300px;
    z-index: 2;
  }
  .offer-badge .brush { font-family: var(--brush); font-weight: 400; }
  .offer-badge .small { font-family: var(--sans); font-weight: 700; }
</style>
</head>
<body>
  <main class="flyer">
    <div class="hero-photo" role="img" aria-label="Foto: selbstbewusste Frau mit gepunktetem Haartuch und gestreiftem Shirt zeigt ihren angespannten Oberarm"></div>

    <div class="logo-box">
      <span class="logo-dot"></span>
      <span class="logo-name">Coaching für<br>Klarmacher</span>
    </div>

    <svg class="headline" viewBox="0 380 600 290" role="heading" aria-level="1" aria-label="Be B.R.A.V.E.">
      <rect x="347" y="391" width="223" height="125" fill="rgba(95,148,22,0.9)"/>
      <rect x="48" y="505" width="522" height="151" fill="rgba(95,148,22,0.9)"/>
      <text x="362" y="510" font-size="112" textLength="172" lengthAdjust="spacingAndGlyphs">BE</text>
      <text x="72" y="634" font-size="116" textLength="498" lengthAdjust="spacingAndGlyphs">B.R.A.V.E.</text>
    </svg>

    <footer class="footer-band">
      <div class="footer-col footer-col--address">
        <p>Dr. Helene Tarwick Coaching</p>
        <p>Lindenweg 14</p>
        <p>35390 Gießhausen</p>
      </div>
      <div class="footer-col footer-col--phone">
        <p><span class="label">Telefon:</span>+49 6401 552184</p>
        <p><span class="label">Mobil:</span>+49 1520 3349071</p>
        <p><span class="label">Fax:</span>06401 552185</p>
      </div>
      <div class="footer-col footer-col--web">
        <p>tarwick@beratung-fuer-klarmacher.de</p>
        <p>www.beratung-fuer-klarmacher.de</p>
      </div>
    </footer>

    <svg class="offer-badge" viewBox="0 0 450 300" aria-label="Jetzt kostenloses Beratungsgespräch unter 01520 33 49 071 vereinbaren!">
      <circle cx="221" cy="150" r="130" fill="#7ab51d" stroke="#ffffff" stroke-width="3"/>
      <text class="small" x="223" y="56" text-anchor="middle" fill="#ffffff" font-size="17" transform="rotate(-8 223 56)">Jetzt</text>
      <g transform="rotate(-10 221 140)">
        <polygon points="92,86 348,86 344,128 96,128" fill="#ffffff"/>
        <polygon points="14,134 434,134 430,178 18,178" fill="#ffffff"/>
        <text class="brush" x="108" y="120" fill="#7ab51d" font-size="32" textLength="226" lengthAdjust="spacingAndGlyphs">KOSTENLOSES</text>
        <text class="brush" x="30" y="169" fill="#7ab51d" font-size="32" textLength="390" lengthAdjust="spacingAndGlyphs">BERATUNGSGESPRÄCH</text>
      </g>
      <g transform="rotate(-10 221 222)" fill="#ffffff" text-anchor="middle">
        <text class="small" x="221" y="216" font-size="17">unter 01520 33 49 071</text>
        <text class="small" x="227" y="238" font-size="17">vereinbaren!</text>
      </g>
    </svg>
  </main>
</body>
</html>
```